BEACH CLUB OPENING INVITATION & FLYER DESIGN

Hi! I need a posh opening poster design for a new upscale beach club we are opening in Bodrum/Turkey. The text should be in english and turkish. Written text on the invitation and flyer should be:
Title: GRAND OPENING PARTY (Only written in English)
Date & Time: 28.05.2016 - 21:00
Address: Yalıkavak Mahallesi Menekşe Sokak No: 5, Bodrum, Muğla / Türkiye
Website: www.lorvanbeachclub.com
Email: info@lorvanbeachclub.com
Tel: +90 (252) 764 18 27
Follow Us / Bizi Takip Edin
Instagram: /lorvanbeachclub
Facebook: /lorvanbeachclub
P.S: I attached the logo and some sample posters
Best of Luck

```html
<!DOCTYPE html>
<html lang="en">
<head>
<meta charset="utf-8">
<title>Lorvan Beach Club – Grand Opening Party</title>
<link href="https://fonts.googleapis.com/css2?family=Montserrat:wght@300;400;500;700&display=swap" rel="stylesheet">
<style>
  :root {
    --page-bg: #f4f4f4;
    --paper: #ffffff;
    --ink: #0b0b0b;
    --ink-on-dark: #ffffff;
    --accent-yellow: #f0dc00;
    --orb-light: #f6f7f8;
    --orb-mid: #9aa0a8;
    --orb-dark: #1b1f27;
    --sea-glow: #fff8ea;
    --sea-gold: #b39a74;
    --sea-deep: #26262f;
  }
  * { margin: 0; padding: 0; box-sizing: border-box; }
  html, body {
    width: 1200px; height: 1200px; overflow: hidden;
    background: var(--page-bg);
    font-family: "Montserrat", sans-serif;
  }
  .flyer {
    position: absolute;
    left: 189px; top: 49px;
    width: 835px; height: 1079px;
    background: var(--paper);
    overflow: hidden;
  }
  .event-date {
    position: absolute; left: 35px; top: 10px;
    font-size: 54px; font-weight: 400; letter-spacing: 0.5px; line-height: 64px;
    color: var(--ink);
  }
  .event-time {
    position: absolute; left: 38px; top: 76px;
    font-size: 22px; font-weight: 400; letter-spacing: 1px;
    color: var(--ink);
  }
  .brand {
    position: absolute; left: 0; right: 0; top: 14px;
    display: flex; flex-direction: column; align-items: center; gap: 10px;
  }
  .brand-dot {
    width: 54px; height: 54px; border-radius: 50%;
    background: var(--ink);
  }
  .brand-name {
    font-size: 19px; font-weight: 400; letter-spacing: 2px;
    color: var(--ink);
  }
  .sea-photo {
    position: absolute; left: 0; right: 0; top: 679px; bottom: 0;
    background:
      radial-gradient(ellipse 60% 30% at 52% 22%, var(--sea-glow) 0%, rgba(255,248,234,0) 100%),
      linear-gradient(to bottom, var(--paper) 0%, #eee9e0 12%, #cbbfa9 30%, var(--sea-gold) 48%, #5e5550 70%, var(--sea-deep) 100%);
  }
  .orb {
    position: absolute; left: 137px; top: 195px;
    width: 568px; height: 568px; border-radius: 50%;
    background: radial-gradient(circle at 52% 62%, var(--orb-light) 0%, #d3d6da 22%, var(--orb-mid) 48%, #4b5058 75%, var(--orb-dark) 100%);
  }
  .headline {
    position: absolute; left: 186px; top: 305px;
    font-weight: 400;
  }
  .headline-sub {
    display: block;
    font-size: 54px; font-weight: 400; letter-spacing: 0.5px;
    color: var(--accent-yellow);
    line-height: 60px;
  }
  .headline-main {
    display: block; margin-top: 2px;
    font-size: 140px; font-weight: 700; letter-spacing: -3px;
    color: var(--ink);
    line-height: 140px;
  }
  .headline-main .thin { font-weight: 300; }
  .address {
    position: absolute; right: 219px; top: 580px;
    text-align: right; font-style: normal;
    font-size: 14px; font-weight: 400; line-height: 19px;
    color: var(--ink);
  }
  .contact {
    position: absolute; left: 0; right: 0; bottom: 26px;
    text-align: center; font-style: normal;
    font-size: 14px; font-weight: 400; line-height: 24px; letter-spacing: 0.3px;
    color: var(--ink-on-dark);
  }
  .contact .follow { font-weight: 500; }
  .contact .sep { padding: 0 10px; opacity: 0.7; }
</style>
</head>
<body>
  <main class="flyer">
    <div class="event-date">28 MAY</div>
    <div class="event-time">2016 · 21:00</div>

    <header class="brand">
      <span class="brand-dot"></span>
      <span class="brand-name">LORVAN BEACH CLUB</span>
    </header>

    <div class="sea-photo" role="img" aria-label="Close-up photo of sparkling sea foam and splashing water glinting in golden sunlight"></div>

    <div class="orb"></div>

    <h1 class="headline">
      <span class="headline-sub">GRAND</span>
      <span class="headline-sub">OPENING</span>
      <span class="headline-main">PART<span class="thin">Y</span></span>
    </h1>

    <address class="address">
      Address<br>
      Yalıkavak Mahallesi<br>
      Menekşe Sokak No: 5,<br>
      Bodrum, Muğla / Türkiye
    </address>

    <address class="contact">
      <div>www.lorvanbeachclub.com<span class="sep">|</span>info@lorvanbeachclub.com<span class="sep">|</span>Tel: +90 (252) 764 18 27</div>
      <div><span class="follow">Follow Us / Bizi Takip Edin</span><span class="sep">|</span>Instagram: /lorvanbeachclub<span class="sep">|</span>Facebook: /lorvanbeachclub</div>
    </address>
  </main>
</body>
</html>
```